Human Resource Consulting practice needs a business card design

We need a business card design (double sided colour) for our Human Resource (HR) consulting practice in regional New South Wales, australia. Our business name is Staffwise Partners. We support small and medium business across the Mid North Coast of New South Wales by providing them with outsourced HR support, services and products to help them achieve compliance with workplace legislation and across all areas of the employment lifecycle from recruitment to termination and everything in between. Our corporate colours are hot pink and black. The final design should communicate professionalism, trust, people focus.
I have attached the current (old) business card for your reference.

Target Market(s)

Business owners and high level managers

Industry/Entity Type

Business

Contact Information for Business Card

Name
Title
Phone no
Mobile no
Address
PO Box
email address
website

Colors
e34197

Requirements
Must have
• Tempate for changing business card personal details including Name, position title, mobile number, email address.
• Keep current logo and colours as per attached
• Logo must be presented in 2 colours or black only not white
Nice to have
• One side logo and graphic only other side logo and personal details
Should not have
• Should not be the same as the current version (attached) but a modern interpretation.
• Does not need a busy reverse side with our list of services as per current version. I feel this is too busy.
• No photos

```html
<!DOCTYPE html>
<html lang="en">
<head>
<meta charset="utf-8">
<title>Staffwise Partners – Business Card</title>
<link rel="stylesheet" href="https://fonts.googleapis.com/css2?family=Open+Sans:wght@400;700&display=swap">
<style>
  :root {
    --hot-pink: #e6118f;
    --ink: #000000;
    --paper: #f4f4f4;
    --muted: #6e6e6e;
    --stage: #d9d9dc;
    --ghost: #a9a9a9;
  }
  * { margin: 0; padding: 0; box-sizing: border-box; }
  html, body {
    width: 1200px; height: 800px; overflow: hidden;
    background: var(--stage);
    font-family: "Open Sans", Arial, sans-serif;
  }
  .stage {
    position: relative; width: 1200px; height: 800px;
    display: flex; align-items: center; justify-content: center; gap: 60px;
  }
  .card {
    position: relative; width: 525px; height: 300px; overflow: hidden;
    box-shadow: 0 6px 18px rgba(0,0,0,0.18);
  }

  /* Front side */
  .card--front { background: var(--paper); }
  .card--front .corner-graphic {
    position: absolute; width: 44px; height: 100px; background: var(--ghost); opacity: 0.7;
  }
  .card--front .corner-graphic--left { left: 0; top: 150px; }
  .card--front .corner-graphic--right { right: 0; top: 165px; }
  .card--front .brand-lockup {
    position: absolute; left: 60px; right: 60px; top: 100px;
    display: flex; align-items: flex-end; justify-content: center; gap: 6px;
  }
  .card--front .brand-name {
    font-weight: 700; font-size: 38px; line-height: 1; color: var(--hot-pink);
    letter-spacing: -0.5px; white-space: nowrap;
  }
  .card--front .brand-mark {
    flex: none; width: 10px; height: 10px; margin-bottom: 4px;
    background: var(--hot-pink);
  }
  .card--front .website {
    position: absolute; left: 0; right: 0; bottom: 58px; text-align: center;
    font-size: 13px; color: #222;
  }

  /* Back side */
  .card--back { background: var(--ink); color: var(--muted); }
  .card--back .person { position: absolute; left: 30px; top: 26px; }
  .card--back .person-name {
    font-weight: 700; font-size: 19px; color: var(--hot-pink); line-height: 1.1;
  }
  .card--back .person-title { font-size: 14px; color: var(--muted); }
  .card--back .brand-name {
    position: absolute; left: 30px; top: 88px;
    font-weight: 700; font-size: 34px; line-height: 1; color: var(--hot-pink);
    white-space: nowrap;
  }
  .contact-block {
    position: absolute; display: flex; align-items: stretch; gap: 8px;
    font-size: 11.5px; line-height: 1.55; white-space: nowrap;
  }
  .contact-block .tab {
    width: 12px; background: var(--hot-pink);
    display: flex; flex-direction: column; align-items: center; justify-content: space-around;
  }
  .contact-block .tab svg { width: 8px; height: 8px; }
  .contact-block--phones { left: 30px; top: 160px; }
  .contact-block--postal { right: 30px; bottom: 30px; }
</style>
</head>
<body>
<main class="stage">
  <section class="card card--front" aria-label="Business card front">
    <div class="corner-graphic corner-graphic--left" role="img" aria-label="Grey decorative graphic"></div>
    <div class="corner-graphic corner-graphic--right" role="img" aria-label="Grey decorative graphic"></div>
    <div class="brand-lockup">
      <h1 class="brand-name">Staffwise Partners</h1>
      <span class="brand-mark" aria-hidden="true"></span>
    </div>
    <p class="website">www.staffwisepartners.com.au</p>
  </section>

  <section class="card card--back" aria-label="Business card back">
    <div class="person">
      <p class="person-name">Mark Ellison</p>
      <p class="person-title">Director</p>
    </div>
    <h2 class="brand-name">Staffwise Partners</h2>

    <div class="contact-block contact-block--phones">
      <div class="tab" aria-hidden="true">
        <svg viewBox="0 0 8 8"><rect x="2" y="0.5" width="4" height="7" rx="1" fill="#000"/></svg>
        <svg viewBox="0 0 8 8"><path d="M1 1h2l1 2-1 1a4 4 0 0 0 2 2l1-1 2 1v2a6 6 0 0 1-7-7z" fill="#000"/></svg>
        <svg viewBox="0 0 8 8"><rect x="0.5" y="2" width="7" height="5" fill="#000"/></svg>
      </div>
      <div class="lines">
        <p>0400 555 218</p>
        <p>02 5550 1247</p>
        <p>02 5550 1248</p>
      </div>
    </div>

    <div class="contact-block contact-block--postal">
      <div class="tab" aria-hidden="true">
        <svg viewBox="0 0 8 8"><path d="M4 0.5a2.6 2.6 0 0 0-2.6 2.6C1.4 5 4 7.5 4 7.5S6.6 5 6.6 3.1A2.6 2.6 0 0 0 4 0.5z" fill="#000"/></svg>
        <svg viewBox="0 0 8 8"><rect x="0.5" y="1.5" width="7" height="5" fill="#000"/></svg>
      </div>
      <div class="lines">
        <p>PO Box 312, Lakeside Bay, NSW 2999</p>
        <p>anna@staffwisepartners.com.au</p>
      </div>
    </div>
  </section>
</main>
</body>
</html>
```